Dog Snacks brand needs a new packaging design

Dear Designers,

We are looking for a packaging expert to design our new line of Dog Snacks which contain a relaxing hemp extract (CBD).

Our company is already selling various relaxing cat & dog products , and we would like this new design to reflect the same "style & feeling" as our current products (see attached instructions).

Technical aspects:
- The packaging is a Stand Up Pouch (12x18.5x7cm - see attached instructions).
- Please follow technical guidelines from printer (see attached instructions).
- The packaging will contain 120g of high-quality, semi-moist dog snacks.
- We will be designing 3 differents variations for 3 different flavours: Chicken, Beef & Liver.
- The packaging will be printed with a matt finish.

Design aspects:
- The design should be compatible with our brand identity (i.e. fluffly, pure, relaxing, positive, clean & natural).
- Soft/rounded shapes are preferred.
- Please use our brand's colors (#3BA384, White & Black).
- Please use our company logo (see attached instructions).
- The design also needs to convey a strong sense of professionalism as we are an animal "healthcare" brand.
- If you want to include a dog picture, we would prefer you to use a picture of our official brand ambassador (see attached instructions).
- We have attached a number of packaging examples which we like a lot. (see attached instructions). Please only use those as general inspiration.
- Only original work (no plagiarism will be accepted).

Please don't hesitate to send us a message if you have any questions about the brand, the product or the design requirements.

We look forward to seeing your designs & working on this together !

Thanks & regards,
Marcus

Dog owners

Pet Care

Sans Serif

• Please see project description.

```html
<!DOCTYPE html>
<html lang="en">
<head>
<meta charset="utf-8">
<title>Verdalis Calmora CBD Treats – Chicken</title>
<link rel="stylesheet" href="https://fonts.googleapis.com/css2?family=Josefin+Sans:wght@400;600;700&family=Roboto+Slab:wght@500&display=swap">
<style>
  :root {
    --brand-teal: #3ba384;
    --teal-deep: #2f9677;
    --teal-light: #8fd3bd;
    --ink: #1c2a22;
    --white: #ffffff;
    --stage: #e9ecec;
  }
  * { box-sizing: border-box; margin: 0; padding: 0; }
  html, body { width: 1200px; height: 1120px; overflow: hidden; }
  body {
    background: var(--stage);
    font-family: "Josefin Sans", Arial, sans-serif;
    position: relative;
  }
  .pouch {
    position: absolute;
    left: 270px; top: 55px;
    width: 660px; height: 1010px;
    border-radius: 42px 42px 14px 14px;
    overflow: hidden;
    background: linear-gradient(180deg, #ffffff 0%, #f3f5f4 100%);
  }
  .pouch-wave { position: absolute; inset: 0; width: 660px; height: 1010px; }
  .pouch > div, .pouch > p { position: absolute; }

  .brand { left: 0; right: 0; top: 118px; text-align: center; }
  .brand-mark {
    display: block; width: 56px; height: 56px; margin: 0 auto 14px;
    border-radius: 50%; border: 3px solid var(--brand-teal);
  }
  .brand-name {
    font-family: "Roboto Slab", Georgia, serif; font-weight: 500;
    font-size: 52px; letter-spacing: 1px; color: var(--ink); line-height: 1;
  }
  .brand-sub {
    left: 0; width: 548px; top: 202px; text-align: right;
    font-family: "Roboto Slab", Georgia, serif; font-size: 19px; color: var(--brand-teal);
  }
  .product-name {
    left: 0; right: 0; top: 258px; text-align: center;
    font-size: 72px; font-weight: 600; color: var(--brand-teal); letter-spacing: 1px; line-height: 1;
  }
  .product-name sup { font-size: 20px; vertical-align: 42px; margin-left: 2px; }
  .product-type {
    left: 205px; width: 224px; top: 340px; text-align: center;
    font-size: 26px; font-weight: 600; letter-spacing: 3px; color: var(--ink);
    border-top: 2px solid var(--ink); border-bottom: 2px solid var(--ink);
    padding: 7px 0 3px;
  }
  .product-dose {
    left: 0; width: 634px; top: 388px; text-align: center;
    font-size: 28px; font-weight: 600; color: var(--brand-teal); letter-spacing: 1px;
  }
  .ambassador-photo {
    left: 38px; top: 428px; width: 312px; height: 524px;
    border-radius: 140px 140px 40px 40px;
    background: linear-gradient(180deg, #e7c8a6 0%, #f4ece2 45%, #3a3a44 70%, #8ed36a 100%);
    opacity: 0.92;
  }
  .flavour { left: 508px; top: 496px; width: 96px; text-align: center; color: var(--white); }
  .flavour-icon {
    display: block; width: 64px; height: 64px; margin: 0 auto 10px;
    border-radius: 50%; border: 3px solid var(--white);
  }
  .flavour-label { font-size: 19px; font-weight: 700; letter-spacing: 0.5px; }
  .thc-free {
    right: 53px; top: 626px; color: var(--white);
    font-size: 30px; letter-spacing: 3px;
  }
  .benefits {
    right: 53px; top: 678px; padding-right: 14px;
    border-right: 3px solid var(--white);
    text-align: right; color: var(--white);
    font-size: 50px; line-height: 49px; letter-spacing: 0.5px;
  }
  .vet-badge {
    left: 298px; top: 750px; width: 124px; height: 124px;
    border-radius: 50%; border: 2px solid rgba(255,255,255,0.85);
  }
  .net-weight {
    right: 57px; top: 868px; color: var(--white);
    font-size: 33px; font-weight: 600;
  }
</style>
</head>
<body>
  <section class="pouch" aria-label="Stand-up pouch front, chicken flavour">
    <svg class="pouch-wave" viewBox="0 0 660 1010" aria-hidden="true">
      <path d="M0 722 C200 600 420 430 660 332 L660 1010 L0 1010 Z" fill="var(--brand-teal)"/>
      <path d="M0 694 C200 574 420 396 660 298" fill="none" stroke="var(--teal-light)" stroke-width="12"/>
    </svg>

    <div class="brand">
      <span class="brand-mark"></span>
      <span class="brand-name">VERDALIS</span>
    </div>
    <p class="brand-sub">For Animals</p>

    <p class="product-name">CALMORA<sup>™</sup></p>
    <p class="product-type">CBD TREATS</p>
    <p class="product-dose">CBD 250MG</p>

    <div class="ambassador-photo" role="img" aria-label="Photo of the brand ambassador corgi standing on a green treat"></div>

    <div class="flavour">
      <span class="flavour-icon"></span>
      <span class="flavour-label">CHICKEN</span>
    </div>

    <p class="thc-free">THC FREE</p>
    <p class="benefits">SUPPORT<br>CALM<br>EASE</p>

    <div class="vet-badge" aria-hidden="true"></div>

    <p class="net-weight">120g NT WT</p>
  </section>
</body>
</html>
```